Spiritual Support flyer design

I offer a range of spiritual support options from a drop in group to meditation. I work alone in two locations, one at home and the other in the local town centre therapy centre. I do not want people to be confused about where to go for each item so thought one side could be the town centre group and the other side of the leaflet could be the things I offer from home. I need to find a way to present a list of things I do and make it look inviting so people want to contact me. I want it to feel inspirational, uplifting, light hearted, with a gentle feel of support or coming home to somewhere safe. The leaflet needs to look eye catching as it will be where there are many other leaflets the same size (A5). I love purples, as they tend to be spiritual colours or the look below of light bursting through the clouds seems appropriate picture wise. I do not have a logo.
The title can be Quiet Harbour. On one side I would like to introduce a Spiritual Experiences drop-in group held at the Larkfield Centre, Colchester 1-2pm every four weeks to share spiritual experiences with others. I can give you more words for that when you are ready. The other side needs to feature the things I offer from my own home which are: Spiritual Counselling, Private email guidance, Meditation one to one, and Quiet Harbour Days, which are like a days retreat. It might be a good idea to mention prices but not in an obvious way, so have that just readable in small print.

Town

```html
<!DOCTYPE html>
<html lang="en">
<head>
<meta charset="utf-8">
<title>Quiet Harbour – Spiritual Support</title>
<link rel="stylesheet" href="https://fonts.googleapis.com/css2?family=Arvo:wght@400;700&family=Arimo:wght@400&display=swap">
<style>
  :root {
    --pink-top: #f38ab0;
    --pink-mid: #e478a6;
    --mauve-bottom: #b9669c;
    --white: #ffffff;
    --lilac: #efd2ee;
    --magenta: #a1327f;
    --soft-white: rgba(255, 255, 255, 0.92);
  }
  * { margin: 0; padding: 0; box-sizing: border-box; }
  html, body { width: 1200px; height: 837px; overflow: hidden; }
  body { background: var(--mauve-bottom); }
  .flyer {
    position: relative;
    width: 1200px;
    height: 837px;
    overflow: hidden;
    font-family: "Arvo", serif;
    color: var(--white);
    background:
      radial-gradient(ellipse 700px 420px at 180px 120px, rgba(255,255,255,0.18), transparent 70%),
      radial-gradient(ellipse 600px 400px at 900px 250px, rgba(255,255,255,0.10), transparent 70%),
      linear-gradient(180deg, var(--pink-top) 0%, var(--pink-mid) 45%, var(--mauve-bottom) 100%);
  }
  .brand {
    position: absolute;
    left: 28px;
    top: 70px;
    display: flex;
    align-items: center;
    gap: 22px;
  }
  .brand-dot {
    width: 118px;
    height: 118px;
    border-radius: 50%;
    background: var(--lilac);
  }
  .brand-name {
    font-family: "Arvo", serif;
    font-weight: 400;
    font-size: 72px;
    line-height: 1;
    color: var(--lilac);
    letter-spacing: 1px;
  }
  .group {
    position: absolute;
    right: 22px;
    top: 128px;
    text-align: right;
  }
  .group-kicker { font-size: 40px; line-height: 1.1; }
  .group-title { font-size: 54px; line-height: 1.05; }
  .where {
    margin-top: 26px;
    font-size: 34px;
    font-weight: 700;
    color: var(--magenta);
    line-height: 1.1;
  }
  .venue, .timing { font-size: 41px; line-height: 1.5; }
  .venue { margin-top: 6px; }
  .group-note {
    font-family: "Arimo", sans-serif;
    font-size: 27px;
    letter-spacing: 0.5px;
    color: var(--soft-white);
  }
  .individual {
    position: absolute;
    left: 16px;
    top: 448px;
  }
  .individual-label {
    font-size: 36px;
    font-weight: 700;
    color: var(--magenta);
    letter-spacing: 1px;
    line-height: 1;
  }
  .services { list-style: none; margin-top: 10px; }
  .service {
    display: flex;
    align-items: center;
    gap: 12px;
    font-size: 52px;
    line-height: 68px;
    padding-left: 20px;
  }
  .service-dot {
    flex: none;
    width: 26px;
    height: 26px;
    border-radius: 50%;
    background: var(--white);
  }
  .service-note {
    position: absolute;
    left: 335px;
    top: 782px;
    font-family: "Arimo", sans-serif;
    font-size: 27px;
    letter-spacing: 1px;
    color: var(--soft-white);
  }
  .contact {
    position: absolute;
    right: 26px;
    top: 656px;
    text-align: right;
  }
  .contact-label {
    font-size: 41px;
    font-weight: 700;
    color: var(--magenta);
    letter-spacing: 1px;
    line-height: 1.1;
  }
  .contact-line {
    font-family: "Arimo", sans-serif;
    font-size: 22px;
    line-height: 28px;
    text-transform: uppercase;
  }
</style>
</head>
<body>
  <main class="flyer">
    <header class="brand">
      <span class="brand-dot"></span>
      <span class="brand-name">Quiet Harbour</span>
    </header>

    <section class="group">
      <p class="group-kicker">Spiritual Experiences</p>
      <h1 class="group-title">drop-in group</h1>
      <p class="where">·WHERE?</p>
      <p class="venue">Larkfield Centre, Colchester</p>
      <p class="timing">1-2pm every four weeks</p>
      <p class="group-note">Share spiritual experiences with others</p>
    </section>

    <section class="individual">
      <h2 class="individual-label">OR INDIVIDUAL</h2>
      <ul class="services">
        <li class="service"><span class="service-dot"></span>Spiritual Counselling</li>
        <li class="service"><span class="service-dot"></span>Private email guidance</li>
        <li class="service"><span class="service-dot"></span>Meditation one to one</li>
        <li class="service"><span class="service-dot"></span>Quiet Harbour Days</li>
      </ul>
    </section>
    <p class="service-note">Personalizated attention.</p>

    <section class="contact">
      <h2 class="contact-label">CONTACT</h2>
      <p class="contact-line">Mira Ellison</p>
      <p class="contact-line">Telephone: (001) 00 5678 - 14</p>
      <p class="contact-line">E-mail: hello@quietharbour.example</p>
    </section>
  </main>
</body>
</html>
```